" A Turma da Brasa integra 03 personas: Restaurantes, Empresas e Funcionários dessas empresa. A Turma da Brasa fecha parcerias com RESTAURANTES para que eles aceitem o pagamento através do Turma da Brasa. O pagamento é feito pelo próprio aplicativo através de um QR CODE ou um cartãozinho físico de vale-refeição (que tem um QR CODE). Para o restaurante participar do Turma da brasa, ele tem que dar 10% de desconto a quem o Turma da Brasa levar lá para almoçar. A Empresa (para quem faremos essa arte), é para quem queremos "vender" o vale-refeição. As empresas, hoje, utilizam geralmente PIRUNA, CAVORI, QUIVEL e KZ, mas essas fornecedoras não dão qualquer tipo de benefício aos funcionários das empresas, se não a questão da utilização do KZ! O usuário é o funcionário da empresa, que receberá vale-refeição (a este também será destinado esse material). O usuário terá um aplicativo em que poderá buscar o prato que deseja comer (Ex: Bife à role), ou a cozinha que deseja (italiana, brasiileira), ver nas imediações os restaurantes que atendem ao filtro realizado, pagar com o celular (diretamente ao garçon, sem precisar levantar da mesa), e terá 10% de desconto em toda rede "

```html
<!DOCTYPE html>
<html lang="pt-BR">
<head>
<meta charset="utf-8">
<title>Turma da Brasa – Benefício para Empresas</title>
<link href="https://fonts.googleapis.com/css2?family=Montserrat:wght@500;700;800;900&display=swap" rel="stylesheet">
<style>
  :root {
    --page-bg: #e9e6e3;
    --wine: #7a1e2a;
    --wine-deep: #4a1118;
    --amber: #f5b21c;
    --white: #ffffff;
    --photo-warm: #8a6a58;
    --photo-cool: #3b4350;
    --photo-light: #c9b7a6;
  }
  html, body {
    margin: 0;
    width: 1200px;
    height: 1200px;
    overflow: hidden;
    background: var(--page-bg);
    font-family: "Montserrat", sans-serif;
  }
  .artboard {
    position: absolute;
    left: 40px;
    top: 220px;
    width: 1120px;
    height: 760px;
    overflow: hidden;
    border-radius: 6px;
  }
  .team-photo {
    position: absolute;
    inset: 0;
    background:
      radial-gradient(ellipse at 62% 45%, var(--photo-light) 0%, transparent 45%),
      linear-gradient(120deg, var(--photo-warm) 0%, #6d5a52 45%, var(--photo-cool) 100%);
  }
  .brand-overlay {
    position: absolute;
    inset: 0;
    background: linear-gradient(90deg, rgba(122,30,42,0.96) 0%, rgba(122,30,42,0.88) 34%, rgba(122,30,42,0.45) 52%, rgba(122,30,42,0) 72%);
  }
  .bottom-shade {
    position: absolute;
    inset: auto 0 0 0;
    height: 200px;
    background: linear-gradient(0deg, rgba(74,17,24,0.7), rgba(74,17,24,0));
  }
  .frame-line {
    position: absolute;
    inset: 26px 34px 30px 34px;
    border: 2px solid rgba(255,255,255,0.85);
    border-radius: 14px;
  }
  .brand-name {
    position: absolute;
    left: 110px;
    top: 34px;
    display: flex;
    align-items: center;
    gap: 10px;
    color: var(--white);
    font-weight: 800;
    font-size: 24px;
    background: var(--wine);
    padding: 2px 14px;
  }
  .brand-name .dot {
    width: 20px; height: 20px; border-radius: 50%; background: var(--white);
  }
  .headline {
    position: absolute;
    left: 92px;
    top: 240px;
    margin: 0;
  }
  .headline .kicker {
    display: block;
    color: var(--white);
    font-weight: 800;
    font-size: 32px;
    letter-spacing: 0.5px;
  }
  .headline .target {
    display: block;
    color: var(--amber);
    font-weight: 900;
    font-size: 82px;
    line-height: 0.95;
    letter-spacing: -1px;
  }
  .benefits {
    position: absolute;
    left: 92px;
    top: 380px;
    width: 300px;
    display: grid;
    grid-template-columns: 1fr 1fr;
    gap: 22px 20px;
    margin: 0; padding: 0; list-style: none;
  }
  .benefit {
    color: var(--white);
    font-weight: 700;
    font-size: 14px;
    line-height: 1.15;
    text-align: center;
    width: 130px;
  }
  .benefit svg { display: block; margin: 0 auto 8px; }
  .footnotes {
    position: absolute;
    left: 92px;
    top: 640px;
    display: flex;
    gap: 36px;
    color: var(--white);
    font-weight: 600;
    font-size: 13px;
    line-height: 1.3;
  }
  .footnotes p { margin: 0; width: 330px; }
  .social {
    position: absolute;
    right: 90px;
    top: 672px;
    display: flex;
    gap: 20px;
  }
  .social span {
    width: 22px; height: 22px; border-radius: 50%; background: var(--white);
  }
</style>
</head>
<body>
  <main class="artboard">
    <div class="team-photo" role="img" aria-label="Foto de executivos sorridentes em um escritório olhando um tablet"></div>
    <div class="brand-overlay"></div>
    <div class="bottom-shade"></div>
    <div class="frame-line"></div>

    <div class="brand-name"><span class="dot"></span>Turma da Brasa</div>

    <h1 class="headline">
      <span class="kicker">BENEFÍCIO PARA</span>
      <span class="target">EMPRESAS</span>
    </h1>

    <ul class="benefits">
      <li class="benefit">
        <svg width="40" height="40" viewBox="0 0 40 40" fill="none" stroke="#f5b21c" stroke-width="2.5"><rect x="4" y="6" width="26" height="30" rx="3"/><path d="M10 14h14M10 20h14M10 26h8"/><path d="M26 30l10-10"/></svg>
        SEM CUSTO<br>DE ADESÃO
      </li>
      <li class="benefit">
        <svg width="40" height="40" viewBox="0 0 40 40" fill="none" stroke="#f5b21c" stroke-width="2.5"><rect x="5" y="8" width="30" height="27" rx="3"/><path d="M5 16h30M12 4v8M28 4v8M12 23h4M22 23h4M12 29h4"/></svg>
        SEM<br>MENSALIDADE
      </li>
      <li class="benefit">
        <svg width="40" height="40" viewBox="0 0 40 40" fill="none" stroke="#f5b21c" stroke-width="2.5"><rect x="9" y="4" width="22" height="32" rx="3"/><rect x="13" y="8" width="14" height="9"/><path d="M14 23h3M20 23h3M26 23h1M14 29h3M20 29h3"/></svg>
        SEM CUSTO<br>DE TAXAS DE<br>MAQUININHA
      </li>
      <li class="benefit">
        <svg width="40" height="40" viewBox="0 0 40 40" fill="none" stroke="#f5b21c" stroke-width="2.5"><rect x="8" y="17" width="24" height="19" rx="3"/><path d="M13 17v-5a7 7 0 0 1 14 0"/><circle cx="20" cy="26" r="2.5"/></svg>
        SEM<br>FIDELIDADE
      </li>
    </ul>

    <div class="footnotes">
      <p>VOCÊ NÃO PRECISA CANCELAR SEU VALE-REFEIÇÃO ATUAL PARA USAR O TURMA DA BRASA</p>
      <p>CONTATE NOSSOS EXECUTIVOS DE VENDA E VENHA FAZER UM TESTE SEM COMPROMISSO</p>
    </div>

    <div class="social" aria-label="Redes sociais">
      <span></span><span></span><span></span><span></span>
    </div>
  </main>
</body>
</html>
```